Velmora Works Brochure Design Project

Our company requires a brochure for promoting our Corporate Training business.

Please use data from Corporate training brochure doc.

Dear Designers,

We have added new corporate brochure document into the project. Use this data to finish up your brochure.

Thanks,

Omar deswick

Reason: We have recently finalised the data that will go into the corporate brochure.

Reason: To get more better designs

Target Market(s)

Training Managers / Business Managers / Hiring Managers

Industry/Entity Type

Training

Requirements
Must have
• Corporate and Professional Look

```html
<!DOCTYPE html>
<html lang="en">
<head>
<meta charset="utf-8">
<title>Velmora Works Corporate Training Brochure Cover</title>
<link rel="stylesheet" href="https://fonts.googleapis.com/css2?family=Cormorant+SC:wght@500&display=swap">
<style>
  :root {
    --slate-teal: #4e6a6a;
    --slate-teal-deep: #3c5656;
    --mosaic-light: #d3dcdc;
    --mosaic-mid: #95abab;
    --mosaic-dark: #6e8787;
    --panel-grey: #5b6065;
    --panel-navy: #1d232b;
    --gold: #f2b705;
    --gold-deep: #c98d00;
    --label-white: #f1f2f2;
  }
  html, body {
    margin: 0;
    padding: 0;
    overflow: hidden;
    background: #ffffff;
  }
  .brochure-cover {
    position: relative;
    width: 857px;
    height: 1200px;
    overflow: hidden;
    background: var(--slate-teal);
  }
  .cover-curls {
    position: absolute;
    inset: 0;
  }
  .feature-band {
    position: absolute;
    left: 0;
    top: 328px;
    width: 857px;
    height: 415px;
  }
  .team-photo {
    position: absolute;
    left: 0;
    top: 0;
    width: 580px;
    height: 415px;
    background: linear-gradient(100deg, #2a2e33 0%, #6d6560 30%, #b9a89e 55%, #9fb58c 78%, #d9e3d0 100%);
  }
  .accent-bar {
    position: absolute;
    top: 152px;
    height: 42px;
    background: linear-gradient(180deg, var(--gold) 0%, var(--gold-deep) 100%);
  }
  .accent-bar--left { left: 0; width: 100px; }
  .accent-bar--right { left: 580px; width: 277px; }
  .identity-panel {
    position: absolute;
    left: 580px;
    top: 0;
    width: 277px;
    height: 415px;
  }
  .identity-panel__name-block {
    position: absolute;
    left: 0; top: 0;
    width: 100%;
    height: 172px;
    background: var(--panel-grey);
  }
  .identity-panel__logo-block {
    position: absolute;
    left: 0; top: 172px;
    width: 100%;
    height: 243px;
    background: var(--panel-navy);
  }
  .identity-label {
    position: absolute;
    left: 0;
    width: 100%;
    margin: 0;
    text-align: center;
    font-family: "Cormorant SC", "Times New Roman", serif;
    font-weight: 500;
    font-size: 34px;
    line-height: 38px;
    color: var(--label-white);
  }
  .identity-label--name { top: 42px; }
  .identity-label--logo { top: 258px; }
</style>
</head>
<body>
  <main class="brochure-cover">
    <svg class="cover-curls" width="857" height="1200" viewBox="0 0 857 1200" aria-hidden="true">
      <defs>
        <linearGradient id="mosaicTop" x1="0" y1="0" x2="0" y2="1">
          <stop offset="0" stop-color="#a8bcbc"/>
          <stop offset="0.55" stop-color="var(--mosaic-light)"/>
          <stop offset="1" stop-color="#e2e8e8"/>
        </linearGradient>
        <linearGradient id="mosaicBottom" x1="0" y1="0" x2="1" y2="1">
          <stop offset="0" stop-color="var(--mosaic-light)"/>
          <stop offset="0.5" stop-color="var(--mosaic-mid)"/>
          <stop offset="1" stop-color="var(--mosaic-dark)"/>
        </linearGradient>
      </defs>
      <path class="curl-top" d="M95,0 H770 C720,110 690,240 690,330 H165 C165,240 140,110 95,0 Z" fill="url(#mosaicTop)"/>
      <path class="curl-bottom-back" d="M590,743 H700 C670,880 650,1040 690,1200 H60 L120,1140 C300,1010 500,870 590,743 Z" fill="var(--slate-teal-deep)"/>
      <path class="curl-bottom-face" d="M100,743 H590 C500,870 300,1010 120,1140 C105,1010 110,870 100,743 Z" fill="url(#mosaicBottom)"/>
    </svg>

    <section class="feature-band">
      <div class="team-photo" role="img" aria-label="Photograph of a smiling business team standing in a line in a bright office corridor"></div>
      <div class="accent-bar accent-bar--left"></div>
      <div class="identity-panel">
        <div class="identity-panel__name-block"></div>
        <div class="identity-panel__logo-block"></div>
        <p class="identity-label identity-label--name">Company<br>Name</p>
        <p class="identity-label identity-label--logo">Company<br>Logo</p>
      </div>
      <div class="accent-bar accent-bar--right"></div>
    </section>
  </main>
</body>
</html>
```